Poster for a 100 y.o. Tennis Tournament

I would like a poster designed to promote our tennis tournament but I'd like to avoid some of the clichés like the shadow of a player serving. Just well styled text would be fine but some clever imagery would be a bonus.
Highlighting the fact our tournament has been running for over 100 years would be nice so a retro design would work. But that doesn't mean a modern design, for example a minimalist approach utilising the lines of a tennis court, wouldn't work.
Updates

Our tennis committee is now in the process of short listing and will provide an update within 48 hours.

Industry/Entity Type

Court

Requirements
Must have
• The poster must contain the following text at a minimum:
"Marbury Tennis Tournament"/"Since 1908"
"9 March - 11 March, 2013" or "9-11 March, 2013", etc
"www.marburytennis.com.au"

The poster must be reproducible in colour and black & white, or at least have an alternate for black & white.

The poster must be usable in both A3 and A4 sizes.
Nice to have
• The poster should contain the following text:
"Championship"
"Handicap"
"Seniors"
"Juniors"
Each above may be optionally succeeded by "Singles & Doubles", e.g. "Championship Singles & Doubles". It would actually be clearer if this additional text was used but would be repetitive, so alternate text "Singles & Doubles in all categories" might also be used. Alternatives for variety (with the first word the focus): "Championship Singles & Doubles", "Handicap Singles & Doubles", "Seniors 35+ & 50+", "Juniors 18&U, 14&U"

Ideally the poster will provision room for four to eight sponsors logos, preferably at the bottom, but failure to do this is not a show stopper.

The following text may also be used:
"Entries close February 24"
"Tollard Plate Weekend"

Attached is a photo of one of the old trophies. Utilisation of the curved style of the "Marbury Tennis Tournament" text would fit in with the history if the tournament.

The ability to reuse elements of the poster in a single page website used to promote the tournament would be an advantage (as it will provide consistency).

If you could have an image of a tennis ball that conveys the same energy as the clock/tyre image in the attached "Under the Glass Moon" poster, that would be cool. Or using split imagery of a wooden racquet and a modern racquet, but with some energy, would also be good. These are just ideas though and by no means essential.

I've also attached a photo of a t-shirt with a poster layout I thought looked good.

Some additional text that can be used:
"Brand new courts"
"Brindle Park, Oakhurst Tce, Marbury"
"Phone 0427 318 642"
"Prizes and Trophies"

```html
<!DOCTYPE html>
<html lang="en">
<head>
<meta charset="utf-8">
<title>Marbury Tennis Tournament 2013</title>
<link rel="stylesheet" href="https://fonts.googleapis.com/css2?family=Anton&family=Open+Sans:wght@400;700&display=swap">
<style>
  :root {
    --paper: #ffffff;
    --court-red: #f51a06;
    --title-cyan: #4ef2e6;
    --ink: #111111;
    --ball-yellow: #fff21a;
    --ball-deep: #e8c600;
    --ball-rim: #111111;
    --display: "Anton", "Oswald", sans-serif;
    --body: "Open Sans", Arial, sans-serif;
  }
  * { margin: 0; padding: 0; box-sizing: border-box; }
  html, body { width: 900px; height: 1200px; overflow: hidden; background: var(--paper); }
  .poster { position: relative; width: 900px; height: 1200px; background: var(--paper); }
  .field {
    position: absolute; left: 6px; top: 6px; width: 888px; height: 1106px;
    background: var(--court-red); overflow: hidden;
  }
  .tilted { position: absolute; transform: translate(-50%, -50%) rotate(-13deg); white-space: nowrap; }
  .date-tag {
    left: 252px; top: 126px;
    background: var(--paper); color: var(--ink);
    font-family: var(--display); font-size: 46px; line-height: 1;
    padding: 8px 18px 10px;
  }
  .title-main {
    left: 276px; top: 218px;
    color: var(--title-cyan); font-family: var(--display);
    font-size: 122px; line-height: 1; letter-spacing: 1px;
  }
  .title-sub {
    left: 318px; top: 322px;
    color: var(--title-cyan); font-family: var(--display);
    font-size: 64px; line-height: 1;
  }
  .since {
    left: 348px; top: 404px;
    color: var(--paper); font-family: var(--display);
    font-size: 50px; line-height: 1;
  }
  .ball { position: absolute; border-radius: 50%;
    background: radial-gradient(circle at 40% 35%, var(--ball-yellow) 0 60%, var(--ball-deep) 100%);
    border: 10px solid var(--ball-rim); }
  .ball--tiny { left: 600px; top: 46px; width: 108px; height: 108px; border-width: 6px; }
  .ball--small { left: 624px; top: 242px; width: 148px; height: 148px; border-width: 8px; }
  .ball--medium { left: 374px; top: 446px; width: 334px; height: 334px; border-width: 12px; }
  .ball--large { left: 48px; top: 570px; width: 516px; height: 516px; border-width: 18px; }
  .events {
    position: absolute; right: 36px; top: 772px; text-align: right;
    color: var(--paper); font-family: var(--body); font-size: 26px; line-height: 38px;
  }
  .events .category { font-weight: 700; margin-top: 12px; }
  .events .category:first-child { margin-top: 0; }
  .events .detail { margin-bottom: 8px; }
  .web {
    position: absolute; right: 36px; top: 1066px;
    color: var(--paper); font-family: var(--body); font-size: 21px;
  }
  .sponsors {
    position: absolute; left: 0; right: 0; top: 1140px; text-align: center;
    color: var(--ink); font-family: var(--body); font-size: 24px;
  }
</style>
</head>
<body>
  <main class="poster">
    <section class="field">
      <div class="ball ball--tiny" role="img" aria-label="Illustrated tennis ball"></div>
      <div class="ball ball--small" role="img" aria-label="Illustrated tennis ball"></div>
      <div class="ball ball--medium" role="img" aria-label="Illustrated tennis ball"></div>
      <div class="ball ball--large" role="img" aria-label="Large illustrated tennis ball"></div>

      <p class="tilted date-tag">9-11 March, 2013</p>
      <h1 class="tilted title-main">MARBURY</h1>
      <h2 class="tilted title-sub">TENNIS TOURNAMENT</h2>
      <p class="tilted since">Since 1908</p>

      <div class="events">
        <p class="category">Championship</p>
        <p class="detail">Singles &amp; Doubles</p>
        <p class="category">Handicap</p>
        <p class="detail">Singles &amp; Doubles</p>
        <p class="detail">Seniors 35+ &amp; 50+</p>
        <p class="detail">Juniors 18 &amp; U, 14 &amp; U</p>
      </div>
      <p class="web">www.marburytennis.com.au</p>
    </section>
    <p class="sponsors">Sponsors logos</p>
  </main>
</body>
</html>
```